Business Card Design

hello Guys,
We need a double sided business card. Would like a clean and modern look. Simple, clean, elegant.

Front:
Logo/Company name or Logo/Products
Back:
Contact details

You can go to our website for color scheme.

Information for the business cards are as follows:
Our logo (it is attached)
Products: Divisórias, Forros, Persianas, Pisos
The Company name is: Lumen Painéis
Name: Rodrigo Matheus Valente
Position: Diretor Comercial
Tel: 11 3917-4482 / 95827-6043 / ID: 48*17*26584
Email: contato@lumenpaineis.com.br
Web: www.lumenpaineis.com.br
Address: R: Otávio Brandão 83 – São Paulo – CEP: 04718-230

The card should be of 85mm x 55mm
The winner will deliver:

1) JPG, PNG, TIFF, PDF, Ai, EPS, PSD format files.
The work product will be an Illustrator or Photoshop file
Good luck and let me know if you have any other questions.

CMYK, 300 dpi, convert fonts into paths (vector paths)
set margins at least 4 mm away from the edges

Thanks

```html
<!DOCTYPE html>
<html lang="pt-BR">
<head>
<meta charset="utf-8">
<title>Lumen Painéis — Cartão de visita</title>
<link rel="stylesheet" href="https://fonts.googleapis.com/css2?family=Lato:wght@400;700&display=swap">
<style>
  :root {
    --stage: #2a2a2a;
    --paper: #ffffff;
    --paper-shade: #ececec;
    --orange: #ef8a23;
    --grey: #9b9b9b;
    --ink: #5a5a5a;
  }
  html, body {
    margin: 0;
    width: 1200px;
    height: 800px;
    overflow: hidden;
    background: var(--stage);
    font-family: "Lato", Arial, sans-serif;
  }
  .stage {
    position: relative;
    width: 1200px;
    height: 800px;
  }
  .card {
    position: absolute;
    top: 232px;
    width: 520px;
    height: 336px;
    border-radius: 18px;
    overflow: hidden;
    box-shadow: 0 12px 30px rgba(0,0,0,.45);
  }
  .card svg { display: block; }
  .card--contact { left: 50px; }
  .card--brand { left: 630px; }
  .brand-name { font-family: "Lato", Arial, sans-serif; font-weight: 700; fill: var(--orange); }
  .person-name { font-weight: 700; fill: var(--orange); font-size: 17px; }
  .person-role { fill: var(--ink); font-size: 14px; }
  .contact-line { fill: var(--ink); font-size: 13px; }
  .product-list { fill: var(--paper); font-size: 12px; letter-spacing: .5px; }
  .icon { fill: var(--orange); }
</style>
</head>
<body>
<main class="stage">

  <!-- Contact side -->
  <section class="card card--contact" aria-label="Verso do cartão com contatos">
    <svg width="520" height="336" viewBox="0 0 520 336" xmlns="http://www.w3.org/2000/svg">
      <defs>
        <linearGradient id="paperFade" x1="0" y1="0" x2="1" y2="1">
          <stop offset="0" stop-color="var(--paper)"/>
          <stop offset="1" stop-color="var(--paper-shade)"/>
        </linearGradient>
      </defs>
      <rect width="520" height="336" fill="url(#paperFade)"/>

      <!-- bottom swoosh -->
      <path d="M0,236 C150,296 330,306 520,280 L520,336 L0,336 Z" fill="var(--grey)"/>
      <path d="M0,248 C150,310 330,320 520,294 L520,336 L0,336 Z" fill="var(--orange)"/>

      <!-- brand -->
      <circle cx="52" cy="56" r="14" fill="var(--orange)"/>
      <text class="brand-name" x="76" y="67" font-size="30">Lumen Painéis</text>

      <!-- person + divider -->
      <text class="person-name" x="492" y="116" text-anchor="end">Rodrigo Matheus Valente</text>
      <line x1="60" y1="123" x2="492" y2="123" stroke="var(--orange)" stroke-width="2"/>
      <text class="person-role" x="492" y="142" text-anchor="end">Diretor Comercial</text>

      <!-- icons -->
      <path class="icon" d="M33,102 l4,-2 l3,5 l-2,2 q2,4 6,6 l2,-2 l5,3 l-2,4 q-10,0 -16,-16 z"/>
      <path class="icon" d="M33,146 l17,-8 l-6,15 l-3,-5 z"/>
      <g transform="translate(41,163)">
        <circle r="7" fill="none" stroke="var(--orange)" stroke-width="1.6"/>
        <ellipse rx="3" ry="7" fill="none" stroke="var(--orange)" stroke-width="1.2"/>
        <line x1="-7" y1="0" x2="7" y2="0" stroke="var(--orange)" stroke-width="1.2"/>
      </g>
      <path class="icon" d="M41,190 a6,6 0 0 1 6,6 c0,5 -6,11 -6,11 c0,0 -6,-6 -6,-11 a6,6 0 0 1 6,-6 z M41,194 a2,2 0 1 0 0.01,0 z"/>

      <!-- contacts -->
      <text class="contact-line" x="60" y="116">11 3917-4482</text>
      <text class="contact-line" x="60" y="138">95827-6043</text>
      <text class="contact-line" x="60" y="154">ID: 48*17*26584</text>
      <text class="contact-line" x="60" y="170">contato@lumenpaineis.com.br</text>
      <text class="contact-line" x="60" y="186">www.lumenpaineis.com.br</text>
      <text class="contact-line" x="60" y="204">R: Otávio Brandão 83 – São Paulo</text>
      <text class="contact-line" x="60" y="220">CEP: 04718-230</text>
    </svg>
  </section>

  <!-- Brand side -->
  <section class="card card--brand" aria-label="Frente do cartão com a marca">
    <svg width="520" height="336" viewBox="0 0 520 336" xmlns="http://www.w3.org/2000/svg">
      <defs>
        <linearGradient id="paperFadeBrand" x1="0" y1="0" x2="1" y2="1">
          <stop offset="0" stop-color="var(--paper)"/>
          <stop offset="1" stop-color="var(--paper-shade)"/>
        </linearGradient>
      </defs>
      <rect width="520" height="336" fill="url(#paperFadeBrand)"/>

      <!-- end bands -->
      <rect x="0" y="0" width="34" height="336" fill="var(--orange)"/>
      <rect x="486" y="0" width="34" height="336" fill="var(--orange)"/>
      <text class="product-list" transform="translate(22,168) rotate(-90)" text-anchor="middle">Divisórias | Forros | Persianas | Pisos</text>

      <!-- brand -->
      <circle cx="122" cy="168" r="20" fill="var(--orange)"/>
      <text class="brand-name" x="154" y="183" font-size="42">Lumen Painéis</text>
    </svg>
  </section>

</main>
</body>
</html>
```